The Fern Barrel Pub- restaurant menu, new launch

This is a new restaurant launching Summer 2017. Restaurant is a conversion of long standing small town existing family pizza/italian restaurant. new concept shifts concept to a family pub atmosphere featuring familiar appetizers, burgers, wood-fired pizza, and daily specials, draft beer, full- bar.

atmosphere is casual. want menu to reflect a more current "vibe" than the old place did. Not cold and modern, but retain the cozy familiar feel, without seeming dated and old fashioned.

4 panel menu; 8.5 X 11; 2-4 color
Updates

Project Deadline Extended
Reason: I am interested in seeing more designs. I will be providing feedback in the next few days on all designs submitted. I will also be increasing the budget.

Target Market(s)

Family-Oriented Pub, rural location Berkshire County, MA. Mostly Blue collar customer, value oriented

Industry/Entity Type

American Restaurant

Font styles to use
Sans Serif

Colors

Designer to choose colors to be used in the design.

Requirements
Must have
• Clear, uncluttered design, Highlighted items as specified in draft file (to come)
• ability to make changes daily as menu changes
• each panel separate sheet to slide into binder sleeve

```html
<!DOCTYPE html>
<html lang="en">
<head>
<meta charset="utf-8">
<title>The Fern Barrel Pub – Menu</title>
<link href="https://fonts.googleapis.com/css2?family=Montserrat:wght@600;800;900&family=Crimson+Text:ital,wght@0,400;0,600;1,400&family=Pinyon+Script&display=swap" rel="stylesheet">
<style>
  :root{
    --backdrop:#1c2126;
    --paper:#d9ccb3;
    --paper-light:#e2d7c1;
    --paper-dark:#c9b999;
    --ink:#2d2823;
    --ink-soft:#4a4239;
    --art:#5a4f44;
    --art-light:#a89a83;
  }
  *{box-sizing:border-box;margin:0;padding:0}
  html,body{width:1200px;height:1200px;overflow:hidden}
  body{background:var(--backdrop);position:relative;font-family:"Crimson Text",Georgia,serif;color:var(--ink)}
  .menu-sheet{
    position:absolute;top:180px;width:540px;height:840px;
    background:radial-gradient(ellipse at 40% 35%,var(--paper-light),var(--paper) 55%,var(--paper-dark));
    padding:34px 30px;
  }
  .sheet-starters{left:45px}
  .sheet-pizza{left:615px}
  .section-title{font-family:"Montserrat",Arial,sans-serif;font-weight:900;text-transform:uppercase;line-height:.95;letter-spacing:.5px;color:var(--ink)}
  .price-tag{font-family:"Montserrat",Arial,sans-serif;font-weight:800;font-size:11px;text-align:center}
  .item-desc{font-size:11.5px;line-height:1.2;color:var(--ink-soft)}
  .rule{width:14px;height:2px;background:var(--ink);margin:12px auto 10px}
  .opt-list{list-style:none;font-size:11.5px;line-height:1.25;color:var(--ink-soft)}
  .opt-list li::before{content:": "}
  .opt-grid{display:grid;grid-template-columns:1fr 1fr;column-gap:8px}
  .art-slot{background:radial-gradient(ellipse,var(--art-light),rgba(168,154,131,0) 72%)}

  /* starters sheet */
  .starters-cols{display:grid;grid-template-columns:1fr 1fr;column-gap:26px;height:100%}
  .starter-block{text-align:center}
  .starter-block .section-title{font-size:22px}
  .starter-block .item-desc{margin-top:5px}
  .starter-block .opt-list{text-align:left;margin-top:5px}
  .wing-row{display:flex;align-items:center;justify-content:center;gap:8px}
  .wing-art{width:34px;height:28px}
  .burger-art{width:70px;height:58px;margin:0 auto 4px}
  .burger-sub{font-family:"Montserrat",Arial,sans-serif;font-weight:800;font-size:11px;margin-top:8px;line-height:1.2}
  .build-title{font-family:"Montserrat",Arial,sans-serif;font-weight:800;font-size:10px;line-height:1.25;margin-top:10px}
  .addon-table{width:100%;font-size:11px;color:var(--ink-soft);border-collapse:collapse;margin-top:4px}
  .addon-table td{padding:1px 2px}
  .addon-table td:nth-child(even){text-align:right}

  /* pizza sheet */
  .pizza-cols{display:grid;grid-template-columns:250px 1fr;column-gap:20px;height:100%}
  .pizza-title{font-size:40px;letter-spacing:1px}
  .pizza-intro{font-size:12px;line-height:1.2;color:var(--ink-soft);margin-top:12px;text-align:center}
  .oven-art{height:230px;border-radius:50% 50% 10px 40%;background:radial-gradient(ellipse at 45% 45%,var(--art) 0%,#6b5f52 55%,rgba(107,95,82,.3) 80%,rgba(107,95,82,0) 100%);margin-top:40px}
  .specialty-box{border:1.5px dashed var(--ink-soft);padding:10px 12px;text-align:center;margin-top:18px}
  .box-head{font-family:"Montserrat",Arial,sans-serif;font-weight:800;font-size:11px}
  .box-price{font-size:12px}
  .pie-name{font-family:"Montserrat",Arial,sans-serif;font-weight:800;font-size:13px;margin-top:8px;text-transform:uppercase}
  .feast-art{height:140px;margin-top:14px}
  .build-col{text-align:center;margin-top:18px}
  .build-head{font-family:"Montserrat",Arial,sans-serif;font-weight:800;font-size:12px;text-transform:uppercase;margin-top:8px}
  .build-col .item-desc{font-size:12px}
  .script-note{font-family:"Pinyon Script",cursive;font-size:20px;margin-top:8px;line-height:1.1}
</style>
</head>
<body>

<section class="menu-sheet sheet-starters" aria-label="Starters, burgers, soups and salads">
  <div class="starters-cols">
    <div class="col">
      <div class="starter-block">
        <div class="wing-row">
          <div class="art-slot wing-art" role="img" aria-label="Engraved chicken wing sketch"></div>
          <h2 class="section-title">Wings</h2>
          <div class="art-slot wing-art" role="img" aria-label="Engraved chicken wing sketch"></div>
        </div>
        <p class="price-tag">$12</p>
        <p class="item-desc">A Baker's Dozen (13) of the biggest, meatiest wings you'll find anywhere. Choose from our sauces:</p>
        <ul class="opt-list opt-grid">
          <li>Buffalo Mild</li><li>Buffalo Hot</li>
          <li>Garlic Parm</li><li>BBQ</li>
          <li>Thai Chili</li><li>Challenge Hot</li>
          <li>Sweet Heat</li><li>Honey Chipotle</li>
        </ul>
      </div>
      <div class="rule"></div>
      <div class="starter-block">
        <h2 class="section-title">Boneless<br>Wings</h2>
        <p class="price-tag">$12</p>
        <p class="item-desc">Why are they called wings? They're not, but they're tasty boneless chicken bites tossed in any of our wing sauces. Same great sauces.</p>
      </div>
      <div class="rule"></div>
      <div class="starter-block">
        <h2 class="section-title">'Chos!!</h2>
        <p class="price-tag">$11</p>
        <p class="item-desc">Tortilla chips and Nacho Cheese, piled high.</p>
        <ul class="opt-list">
          <li>Add Chicken $3</li><li>Add Pulled Pork $3</li><li>Add Chili $3</li>
        </ul>
      </div>
      <div class="rule"></div>
      <div class="starter-block">
        <h2 class="section-title">Soup&amp;Stuff</h2>
        <ul class="opt-list">
          <li>Chowder $6</li><li>Chili $6</li><li>Du Jour $6</li>
        </ul>
      </div>
      <div class="rule"></div>
      <div class="starter-block">
        <h2 class="section-title">Salads</h2>
        <ul class="opt-list">
          <li>Fern Barrel Chopped Salad $12</li><li>Add Chicken $3</li>
          <li>Gorgonzola Salad $12</li><li>Add Chicken $3</li>
        </ul>
      </div>
    </div>

    <div class="col">
      <div class="starter-block">
        <h2 class="section-title">Spinach<br>Artichoke<br>Dip</h2>
        <p class="price-tag">$10</p>
        <p class="item-desc">The good stuff. Real spinach, real artichoke, melted cheese and warm tortilla chips. We make it right here every day.</p>
      </div>
      <div class="rule"></div>
      <div class="starter-block">
        <div class="art-slot burger-art" role="img" aria-label="Engraved burger sketch"></div>
        <h2 class="section-title">Barrel Burgers</h2>
        <p class="item-desc">Our burgers are half pound patties of fresh ground beef, hand formed and grilled to order. Served with fries and a pickle. Accept no substitutes.</p>
        <p class="burger-sub">THE BARREL BURGER<br>"ORIGINAL"</p>
        <p class="price-tag">$10</p>
        <p class="item-desc">Double patties, American cheese, lettuce, tomato, onion and our house sauce on a toasted bun.</p>
        <p class="build-title">WANT TO DO IT YOUR WAY?<br>OVER 1,000 POSSIBILITIES!</p>
        <table class="addon-table">
          <tr><td>Single</td><td>$8</td><td>Double</td><td>$10</td></tr>
          <tr><td>Triple</td><td>$12</td><td>Quad</td><td>$14</td></tr>
        </table>
        <p class="item-desc" style="margin-top:6px">Add lettuce, tomato, onion, pickle – free. Cheese: American, Cheddar, Swiss 75¢ per</p>
        <p class="item-desc" style="margin-top:4px">Vermont Smoked Bacon $1.50 per</p>
        <p class="item-desc" style="margin-top:4px">World Class Hand Cut Fries $2.50</p>
      </div>
    </div>
  </div>
</section>

<section class="menu-sheet sheet-pizza" aria-label="Wood fired pizza">
  <div class="pizza-cols">
    <div class="pizza-left">
      <h1 class="section-title pizza-title">Wood<br>Fired<br>Pizza</h1>
      <p class="pizza-intro">All our dough is made fresh daily in house with just four ingredients: water, flour, salt and yeast. Baked to perfection in the wood oven, Fern Barrel Pizza is the best in the county!</p>
      <div class="specialty-box">
        <p class="box-head">OUR SPECIALTY PIES</p>
        <p class="box-price">Small $13 &nbsp;Large $17</p>
        <p class="pie-name">The Buffalo Bird</p>
        <p class="item-desc">Buffalo sauce, grilled chicken, mozzarella and topped with red onion for just the right finish. Don't like onion? We'll leave it off!</p>
        <p class="pie-name">Chicken 'Q</p>
        <p class="item-desc">House made BBQ sauce from Old Mill Smokehouse. Grilled chicken and mozzarella make this crowd favorite.</p>
        <p class="pie-name">The Hula Hula</p>
        <p class="item-desc">Sliced ham and Pineapple and mozzarella. It doesn't get any better! Ask for coconut if you're feeling crazy!</p>
      </div>
      <div class="art-slot feast-art" role="img" aria-label="Engraved sketch of pizza, wine bottles and vegetables"></div>
    </div>
    <div class="pizza-right">
      <div class="oven-art" role="img" aria-label="Engraved illustration of a brick wood-fired oven"></div>
      <div class="build-col">
        <p class="build-head" style="margin-top:0">Create Your Own</p>
        <p class="item-desc">Small $11 &nbsp;Large $15</p>
        <p class="item-desc">Choose from our</p>
        <p class="build-head" style="margin-top:0">Standard Toppings</p>
        <p class="item-desc">for $2.00:<br>Pepperoni, Onion, Tomato, Garlic, Green Pepper, Mushroom, Sliced or Chopped Tomato, Broccoli, Spinach, Sliced black olives</p>
        <p class="item-desc" style="margin-top:6px">More</p>
        <p class="build-head" style="margin-top:0">Meats</p>
        <p class="item-desc">for $2.50:<br>Meatball, Bacon, Sausage, Chicken, Ham</p>
        <p class="build-head">Specialty Toppings</p>
        <p class="item-desc">for $3.00:<br>Xtra Cheese, Pineapple, Feta, Ricotta, Kalamata Olives, Hot Peppers, Coconut, Artichokes, Sun dried Tomato, Pesto</p>
        <p class="build-head">Gluten Free</p>
        <p class="item-desc">Available in Small size only<br>Add $2.00</p>
        <p class="script-note">Fold It Up!</p>
        <p class="item-desc">Turn your Pizza into a CALZONE specialty or build your own. Same price as a small.</p>
      </div>
    </div>
  </div>
</section>

</body>
</html>
```